The Copperleaf Soiree Company Ltd. Needs a Facebook Design. An Event & Wedding Company

We need a WOW Facebook design. Focusing on catching people's attention. We don't want it all wedding like Facebook because we do want to focus on events too.

We currently have an underconstruction website up. feel free to check it out.

Http://www.thecopperleafsoiree.com

An attachment of our logo is attached below

Be Creative!!

Target Market(s)

Companies & Couples who's getting married or engaged 

Industry/Entity Type

Wedding

Font styles to use
Serif
Sans Serif
Decorative
Script

Colors

Designer to choose colors to be used in the design.

Requirements
Must have
• VERY VERY CREATIVE! CATCHY!
Should not have
• nothing really boring. anything green!

```html
<!DOCTYPE html>
<html lang="en">
<head>
<meta charset="utf-8">
<title>The Copperleaf Soiree – Facebook Cover</title>
<link rel="stylesheet" href="https://fonts.googleapis.com/css2?family=Josefin+Sans:wght@300;400&display=swap">
<style>
  :root {
    --page-bg: #eeeeee;
    --ink: #3a2a22;
    --rule: #4a362b;
    --copper: #b87333;
    --copper-deep: #8f5526;
    --ivory: #fbf4ea;
    --champagne: #efdcc0;
    --blush: #e9c3b4;
    --rose: #c98f86;
    --plum: #7d4f57;
  }
  * { margin: 0; padding: 0; box-sizing: border-box; }
  html, body {
    width: 1200px;
    height: 900px;
    overflow: hidden;
    background: var(--page-bg);
    font-family: "Josefin Sans", sans-serif;
  }
  .canvas {
    width: 1200px;
    height: 900px;
    display: flex;
    align-items: center;
    justify-content: center;
  }
  .cover {
    position: relative;
    width: 1100px;
    height: 408px;
    overflow: hidden;
    box-shadow: 0 2px 10px rgba(0,0,0,0.12);
  }
  .cover-photo {
    position: absolute;
    inset: 0;
    background:
      radial-gradient(ellipse 340px 260px at 18% 38%, rgba(125,79,87,0.75) 0%, rgba(125,79,87,0) 100%),
      radial-gradient(ellipse 320px 220px at 30% 78%, rgba(201,143,134,0.8) 0%, rgba(201,143,134,0) 100%),
      radial-gradient(ellipse 260px 200px at 62% 20%, rgba(239,220,192,0.9) 0%, rgba(239,220,192,0) 100%),
      radial-gradient(ellipse 420px 260px at 84% 78%, rgba(251,244,234,1) 0%, rgba(251,244,234,0) 100%),
      linear-gradient(100deg, var(--plum) 0%, var(--rose) 24%, var(--blush) 48%, var(--champagne) 72%, var(--ivory) 100%);
  }
  .cover-glow {
    position: absolute;
    border-radius: 50%;
    background: radial-gradient(circle, rgba(255,236,214,0.7) 0%, rgba(255,236,214,0) 70%);
  }
  .cover-glow.one { width: 90px; height: 90px; left: 120px; top: 90px; }
  .cover-glow.two { width: 60px; height: 60px; left: 200px; top: 230px; }
  .cover-glow.three { width: 70px; height: 70px; left: 70px; top: 270px; }
  .cover-glow.four { width: 50px; height: 50px; left: 940px; top: 60px; }
  .cover-veil {
    position: absolute;
    top: 0; bottom: 0;
    left: 78px; right: 100px;
    background: linear-gradient(90deg, rgba(255,248,240,0.35), rgba(255,248,240,0.5) 50%, rgba(255,248,240,0.35));
  }
  .brand {
    position: absolute;
    left: 202px;
    width: 693px;
    top: 0;
    height: 100%;
    text-align: center;
    color: var(--ink);
  }
  .brand-rule {
    position: absolute;
    left: 0; right: 0;
    height: 1.5px;
    background: var(--rule);
  }
  .brand-rule.top { top: 84px; }
  .brand-rule.bottom { top: 299px; }
  .brand-mark {
    position: absolute;
    left: 50%;
    top: 287px;
    width: 26px;
    height: 26px;
    margin-left: -13px;
    border-radius: 50%;
    background: radial-gradient(circle at 35% 35%, var(--copper) 0%, var(--copper-deep) 100%);
    box-shadow: 0 0 0 10px rgba(251,244,234,0.95);
  }
  .brand-name {
    position: absolute;
    left: 0; right: 0;
    top: 118px;
    font-weight: 300;
    font-size: 46px;
    letter-spacing: 4px;
    text-transform: uppercase;
    line-height: 1;
    white-space: nowrap;
  }
  .brand-tagline {
    position: absolute;
    left: 0; right: 0;
    top: 212px;
    font-weight: 300;
    font-size: 23px;
    letter-spacing: 21px;
    text-transform: uppercase;
    line-height: 1;
    padding-left: 21px;
    white-space: nowrap;
  }
</style>
</head>
<body>
  <main class="canvas">
    <section class="cover">
      <div class="cover-photo" role="img" aria-label="Warm champagne and blush toned photo of an elegant banquet table with glassware, folded napkins, white chairs and a flower arrangement"></div>
      <div class="cover-glow one"></div>
      <div class="cover-glow two"></div>
      <div class="cover-glow three"></div>
      <div class="cover-glow four"></div>
      <div class="cover-veil"></div>
      <div class="brand">
        <div class="brand-rule top"></div>
        <h1 class="brand-name">The Copperleaf Soiree</h1>
        <p class="brand-tagline">Events &amp; Wedding</p>
        <div class="brand-rule bottom"></div>
        <div class="brand-mark"></div>
      </div>
    </section>
  </main>
</body>
</html>
```